LABEL DESIGN NEEDED FOR Mabel Fenwick Cookies

I am starting a Cookie Company with my daughter Mabel that will begin by making chocolate chip cookies.
These labels will go on a 2.5 by 2x6 clear cellophane bag that we will use to give out samples of our cookies to others to introduce our new- company to them.
I want the label to be 2X3 for both the front and the back.
These labels are for a cookie business starting out by making chocolate chip cookies. We will start out using clear cellophane bags with gold twist ties.
The size of the bags we will be using at first are 2.5x2x6 and 3.5x2x7.5.
Again, the clear cellophane bags will contain chocolate chip cookies that are round and weigh 1.5 oz. each.
On the front of the label I want it to have my logo which says Mabel Fenwick Cookies (see attached) with the name of the cookie (Chocolate Chip) and the weight (3oz.)
On the back of the label I would like the following:
Ingredients: All-purpose Flour, Semisweet Chocolate Chips, Granulated Sugar, Light Brown Sugar, Butter, Egg yolk, Light Corn Syrup, Milk, Vanilla Extract, Baking Soda, Salt
We also need it to say:
These products were manufactured in a facility that processes nuts and other known allergens. i.e. Milk, Eggs, Wheat, Soy
and it needs to have my address:
Hollowmere, New Ashby 11893
I have attached three things which will help the artist:
1.Our company logo (Mabel Fenwick Cookies)
2.A front and back label of a packaging from a cookie company that I really liked and thought was very cute. This should give the artist a start in terms of what direction to head in.
Thank you so much for all your help and just let me know what I need to do next.

```html
<!DOCTYPE html>
<html lang="en">
<head>
<meta charset="utf-8">
<title>Mabel Fenwick Cookies – Back Label</title>
<link rel="stylesheet" href="https://fonts.googleapis.com/css2?family=Milonga&family=Gabriela&family=Playfair+Display:ital,wght@1,600&display=swap">
<style>
  :root {
    --sky: #dde9f5;
    --ink-blue: #2f72c4;
    --ink-grey: #5a5a5a;
    --fence: #86a7d7;
  }
  html, body {
    margin: 0;
    padding: 0;
    overflow: hidden;
    background: var(--sky);
  }
  .label {
    position: relative;
    width: 1200px;
    height: 800px;
    background: var(--sky);
    overflow: hidden;
  }
  .ingredients {
    position: absolute;
    left: 117px;
    top: 64px;
    width: 956px;
    margin: 0;
    font-family: "Milonga", serif;
    font-size: 38px;
    line-height: 66px;
    color: var(--ink-blue);
    text-align: justify;
  }
  .allergen-note {
    position: absolute;
    left: 117px;
    top: 392px;
    width: 499px;
    margin: 0;
    font-family: "Playfair Display", serif;
    font-style: italic;
    font-weight: 600;
    font-size: 25px;
    line-height: 41px;
    color: var(--ink-grey);
    text-align: justify;
    hyphens: manual;
  }
  .address {
    position: absolute;
    left: 716px;
    top: 396px;
    display: flex;
    align-items: flex-start;
    gap: 16px;
  }
  .address-pin {
    width: 28px;
    height: 38px;
    margin-top: 6px;
    flex: none;
  }
  .address-text {
    margin: 0;
    font-family: "Gabriela", serif;
    font-size: 37px;
    line-height: 52px;
    color: var(--ink-grey);
    font-style: normal;
  }
  .fence-band {
    position: absolute;
    left: 0;
    top: 620px;
    width: 1200px;
    height: 180px;
    background: linear-gradient(180deg, var(--fence), #7e9fd1);
  }
</style>
</head>
<body>
  <main class="label">
    <p class="ingredients">Ingredients: All-purpose Flour, Semisweet Chocolate Chips, Granulated Sugar, Light Brown Sugar, Butter, Egg yolk, Light Corn Syrup, Milk, Vanilla Extract, Baking Soda, Salt</p>

    <p class="allergen-note">These products were manufac&shy;tured in a facility that processes nuts and other known allergens. i.e. Milk, Eggs, Wheat, Soy.</p>

    <div class="address">
      <svg class="address-pin" viewBox="0 0 28 38" aria-hidden="true">
        <path d="M14 0C6.3 0 0 6.2 0 13.9 0 24.3 14 38 14 38s14-13.7 14-24.1C28 6.2 21.7 0 14 0z" fill="#5a5a5a"/>
        <circle cx="14" cy="13.5" r="5.5" fill="#dde9f5"/>
      </svg>
      <address class="address-text">Hollowmere, New<br>Ashby 11893</address>
    </div>

    <div class="fence-band" role="img" aria-label="Blue picket fence along the bottom of the label"></div>
  </main>
</body>
</html>
```